Business cards

Looking for business cards. Brannock Diesel Performance is the name.
Business colors are a hunter or forest green(either green could be used) with silver writing and logo.
Would like it to say maintenance, repairs and motor work, specializing in Korvanix, flintdrive and Halbrets diesels somewhere on the card. Probably on the back
Phone number is
Marlo
845-372-0158
Picture attached is the current logo and is on shirts and hoodies. I would prefer that on the front of the card
Looking for business cards. Brannock Diesel Performance is the name. Business colors are a hunter or forest green(either green could be used) with silver writing and logo. Would like it to say maintenance, repairs and motor work, specializing in Korvanix, flintdrive and Halbrets diesels somewhere on the card. Probably on the back Phone number is Marlo 845-372-0158 Picture attached is the current logo and is on shirts and hoodies. I would prefer that on the front of the card

```html
<!DOCTYPE html>
<html lang="en">
<head>
<meta charset="utf-8">
<title>Brannock Diesel Performance – Business Cards</title>
<link rel="stylesheet" href="https://fonts.googleapis.com/css2?family=Saira:wght@400;500;700;800&display=swap">
<style>
  :root {
    --canvas: #2b2724;
    --card: #1f3d2b;
    --card-back: #1a3525;
    --silver: #dfe3e6;
    --silver-soft: #b9c0c4;
    --emboss: #2f5c41;
    --art-front: #a9b1b5;
    --art-back: #274c36;
    --rule: #b9c0c4;
  }
  * { box-sizing: border-box; margin: 0; padding: 0; }
  html, body { width: 1200px; height: 786px; overflow: hidden; }
  body {
    background: var(--canvas);
    font-family: "Saira", sans-serif;
    color: var(--silver);
    position: relative;
  }
  .card {
    position: absolute;
    top: 238px;
    width: 540px;
    height: 310px;
    box-shadow: 0 10px 30px rgba(0,0,0,.45);
    overflow: hidden;
  }
  .card--front { left: 40px; background: var(--card); }
  .card--back  { left: 620px; background: var(--card-back); }

  .brand {
    font-weight: 800;
    text-transform: uppercase;
    line-height: 1.02;
    letter-spacing: .5px;
  }
  .card--front .brand {
    position: absolute;
    left: 34px; top: 28px;
    font-size: 22px;
    color: var(--silver);
  }
  .logo-art {
    position: absolute;
    border-radius: 2px;
  }
  .card--front .logo-art {
    left: 34px; top: 84px;
    width: 230px; height: 92px;
    background: linear-gradient(135deg, var(--art-front), #8d979c);
  }
  .divider {
    position: absolute;
    left: 290px; right: 0; top: 150px;
    height: 1px;
    background: var(--rule);
  }
  .contact {
    position: absolute;
    left: 34px; bottom: 24px;
  }
  .contact__name {
    font-size: 20px;
    font-weight: 700;
    letter-spacing: 1.5px;
    margin-bottom: 8px;
  }
  .contact__row {
    display: flex; align-items: center; gap: 10px;
    font-size: 12.5px; letter-spacing: .8px;
    line-height: 20px;
    color: var(--silver);
  }
  .contact__row svg { width: 12px; height: 12px; fill: var(--silver); flex: none; }

  .card--back .brand {
    position: absolute;
    left: 0; right: 0; top: 30px;
    text-align: center;
    font-size: 30px;
    color: var(--emboss);
  }
  .card--back .logo-art {
    left: 150px; top: 104px;
    width: 240px; height: 84px;
    background: linear-gradient(135deg, var(--art-back), #21432f);
  }
  .services {
    position: absolute;
    left: 0; right: 0; top: 214px;
    text-align: center;
    font-size: 12.5px;
    font-weight: 500;
    letter-spacing: .9px;
    line-height: 24px;
    color: var(--silver);
  }
  .services .dot { margin: 0 8px; }
</style>
</head>
<body>
  <section class="card card--front">
    <div class="brand">Brannock<br>Diesel Performance</div>
    <div class="logo-art" role="img" aria-label="Flag and diesel pickup truck illustration in silver"></div>
    <div class="divider"></div>
    <div class="contact">
      <p class="contact__name">Marlo</p>
      <p class="contact__row">
        <svg viewBox="0 0 12 12"><path d="M1 4c0-2 2-3 5-3s5 1 5 3l-2 1-1-1.5H4L3 5 1 4zm2 2h6l1 5H2l1-5zm3 1.2a1.6 1.6 0 100 3.2 1.6 1.6 0 000-3.2z"/></svg>
        845-372-0158
      </p>
      <p class="contact__row">
        <svg viewBox="0 0 12 12"><path d="M0 2h12v8H0zM1 3v.4l5 3.3 5-3.3V3z"/></svg>
        marlo@brannockmail.com
      </p>
      <p class="contact__row">
        <svg viewBox="0 0 12 12"><path d="M6 0a6 6 0 110 12A6 6 0 016 0zm0 1.2v9.6A4.8 4.8 0 006 1.2z"/></svg>
        www.yourwebsite.com
      </p>
    </div>
  </section>

  <section class="card card--back">
    <div class="brand">Brannock<br>Diesel Performance</div>
    <div class="logo-art" role="img" aria-label="Embossed flag and diesel pickup truck illustration, tone on tone"></div>
    <p class="services">
      Maintenance<span class="dot">•</span>Repairs and motor work<span class="dot">•</span>Specializing in Korvanix<br>
      Flintdrive and Halbrets diesels
    </p>
  </section>
</body>
</html>
```